Web Design Project for a Software & Consulting Company

We have just completed a recent ArtFlock project for a new logo (see attached).
As the next stage of our rebranding we now require a website re-design to complement the new logo.
Our current site, http://www.rigsumsoft.example was built in-house and does not come across as professional as we would like. We supply software and associated services to some of the world’s largest oil companies and we need our site to reflect that level of client.
We will also be posting another design project for brochures, PowerPoint slides and other materials very soon.
We would like designs for…
Home page
Product page
• QTV
• BLZ
• FNQ
Services
News page
About Us page
Contact Us page
Page for mobile devices that gives basic company and product information
Currently the site is small but we intend to increase content to include white papers etc. this should be taken into account when designing the navigation therefore we would prefer navigation through styled text links rather than images.
Colour schemes should broadly be taken from our new logo, where the dark blue and dark green from the left and right sides of the logo are the main colours, but other, brighter accent colours can be used to highlight sections or content.
Dark Blue = C:88, M:55, Y:44, K:28
Dark Green = C:87, M:53, Y:50, K:50
NB: Don’t use the logo on our current site, make sure you use the one attached.
We would prefer the final file format to be a layered PSD.
The site should be clean and professional and communicate the following...
• That we have a great depth and breadth of knowledge about our customers’ business, enabling us to deliver the best systems and solutions.
• That we are a leading provider of cost estimation and control solutions to the oil and gas industry.
• The benefits of our software and consulting services.
• Show that we deliver outstanding customer service and value with a very high level of professionalism
• The site should have no Flash and be able to self-adjust to fit any screen size.
Things to avoid …
• Obvious and clichéd oil industry imagery, no oil rigs
• Cartoon style graphics
Our Background
We are an integrated software and consulting organization specialising in the drilling side of the oil and gas industry. Simply put our software helps companies better understand, predict and communicate the cost of drilling wells.
We have 3 software products and a consulting offering consisting of…
• QTV - Probabilistic time and cost software
• BLZ – Cost tracking and reporting software
• FNQ – (currently known as BoreMemory) – Lessons learned software
• Consulting services
Our systems are in use in over 30 countries with a broad range of clients including: GN, Solvane, Prue, Tolmar, VONI Kelstra, SALVEM and Quorlit.
Our current site can be found at www.rigsumsoft.example
Our main competitors are
• http://www.gavondel.example/
• http://www.mirrowen.example/
• http://www.tbx.example/services/software-solutions/p1-
Our depth of drilling knowledge, quality of software and collaboration with clients differentiate us form the competition.
We strive for very high levels of customer service.
We look forward to receiving your designs!
Updates
Thanks to all the designers who have submitted a design, we appreciate the effort.
We will do our best to give individual feedback on each design but given that many are quite similar we thought we would give some general feedback first.
Nearly all the designs submitted so far have been slight variations on…
-
Top Menu
-
Scrolling Photo Banner
-
4 Columns
-
Body
-
Deep Footer
These designs are well executed but they are basically the same layout as our existing site and while there is nothing inherently wrong with this layout we would like to see some designs that are a bit more innovative and different. We don’t really want just a polished version of our current site.
Thanks again,
RST
Thanks to everyone who has submitted a design, the response has been great.
We are close to making a decision so if you are intending to submit a design please do it soon, the deadline is only a few days away.
Thanks again.
RST
Target Market(s)
Mid to high level executives
Industry/Entity Type
Oil And Gas
Look and feel

```html
<!DOCTYPE html>
<html lang="en">
<head>
<meta charset="utf-8">
<title>Rigsum Software</title>
<link rel="stylesheet" href="https://fonts.googleapis.com/css2?family=Ubuntu:wght@400;500;700&family=Arimo:wght@400;700&display=swap">
<style>
:root{
  --teal:#245f72;
  --teal-dark:#17434f;
  --green:#6d8a3c;
  --green-dark:#52692b;
  --paper:#fafafa;
  --band:#eeeeee;
  --line:#d4d4d4;
  --ink:#444;
  --body:#555;
  --foot:#2a2a2a;
  --foot-bottom:#1d1d1d;
  --foot-text:#8c8c8c;
  --foot-head:#dcdcdc;
}
*{box-sizing:border-box;margin:0;padding:0}
html,body{width:1054px;height:1200px;overflow:hidden;background:var(--paper)}
.page{position:relative;width:1000px;height:1138px;transform:scale(1.054);transform-origin:0 0;font-family:Arimo,Arial,sans-serif;color:var(--body)}
.abs{position:absolute}
.topline{left:0;top:0;width:1000px;height:3px;background:var(--teal)}
.header{left:0;top:3px;width:1000px;height:95px;background:#fff;border-bottom:1px solid #e2e2e2}
.brand{left:125px;top:46px;display:flex;align-items:center;gap:10px;font-family:Ubuntu,sans-serif;font-weight:500;font-size:21px;color:var(--teal);letter-spacing:.5px}
.brand-dot{width:14px;height:14px;border-radius:50%;background:var(--teal)}
.nav{left:426px;top:72px;display:flex;gap:7px}
.nav a{display:block;height:26px;line-height:26px;padding:0 14px;font-family:Ubuntu,sans-serif;font-size:11px;color:#444;text-decoration:none;background:linear-gradient(#fafafa,#e6e6e6);border:1px solid #ccc;border-bottom:none;border-radius:3px 3px 0 0}
.nav a.active{background:var(--teal);color:#fff;border-color:var(--teal)}
.hero{left:125px;top:98px;width:750px;height:345px;background:radial-gradient(ellipse at 35% 40%,#9a9a9a,#6e6e6e 55%,#4c4c4c)}
.hero-person{left:420px;top:0;width:330px;height:345px;background:linear-gradient(90deg,rgba(255,255,255,0),rgba(220,220,225,.35) 40%,rgba(235,235,238,.55))}
.hero-copy{left:34px;top:218px;font-family:Ubuntu,sans-serif;color:#fff;text-shadow:0 1px 3px rgba(0,0,0,.5);line-height:1.2}
.hero-copy .s{font-size:15px}
.hero-copy .b{font-size:22px;font-weight:700}
.arrow{width:36px;height:34px;background:linear-gradient(#f7f7f7,#dcdcdc);border:1px solid #bbb;border-radius:3px;display:flex;align-items:center;justify-content:center;box-shadow:0 1px 2px rgba(0,0,0,.2)}
.band{left:0;top:443px;width:1000px;height:273px;background:var(--band);border-top:1px solid #ddd;border-bottom:1px solid #ddd}
.card{top:491px;width:171px;height:201px;background:#fff;border:1px solid var(--line);border-radius:2px;text-align:center}
.card-icon{position:absolute;left:58px;top:-22px;width:55px;height:55px;border-radius:50%;background:var(--teal);display:flex;align-items:center;justify-content:center}
.ribbon{position:absolute;left:-6px;top:43px;width:181px;height:24px;background:linear-gradient(#2c6c80,var(--teal));color:#fff;font-family:Ubuntu,sans-serif;font-size:15px;line-height:24px}
.ribbon::before,.ribbon::after{content:"";position:absolute;top:24px;border-top:6px solid var(--teal-dark)}
.ribbon::before{left:0;border-left:6px solid transparent}
.ribbon::after{right:0;border-right:6px solid transparent}
.card p{position:absolute;left:8px;right:8px;top:79px;font-size:10.5px;line-height:14px;color:var(--body)}
.btn{position:absolute;left:51px;top:162px;width:69px;height:23px;line-height:23px;background:var(--green);border:1px solid var(--green-dark);border-radius:2px;color:#fff;font-size:10.5px}
.section-title{left:123px;top:739px;display:flex;align-items:center;gap:8px;font-family:Ubuntu,sans-serif;font-weight:400;font-size:19px;color:var(--ink)}
.ring{width:22px;height:22px;border-radius:50%;background:var(--teal);display:flex;align-items:center;justify-content:center}
.clients{left:123px;top:779px;width:755px;height:84px;background:#fff;border:1px solid var(--line);border-radius:2px}
.client{top:793px;width:101px;height:54px;border:1px solid #e0e0e0;background:#fff;display:flex;align-items:center;justify-content:center;font-family:Ubuntu,sans-serif;font-weight:500;font-size:13px;color:#555}
.footer{left:0;top:886px;width:1000px;height:188px;background:var(--foot);border-top:2px solid #111}
.col-head{top:912px;display:flex;align-items:center;gap:10px;font-family:Ubuntu,sans-serif;font-size:20px;color:var(--foot-head)}
.divider{top:912px;width:1px;height:145px;background:#3a3a3a}
.foot-text{font-size:10px;line-height:14px;color:var(--foot-text)}
.about p{text-align:justify}
.news li{list-style:none;margin-bottom:14px;padding-left:11px;position:relative}
.news li::before{content:"›";position:absolute;left:0;color:#666}
.contact .foot-text{font-size:9.5px}
.office{font-family:Ubuntu,sans-serif;font-size:14px;color:var(--foot-head);display:flex;align-items:center;gap:6px}
.row{display:flex;align-items:center;gap:10px}
.bottom{left:0;top:1074px;width:1000px;height:64px;background:var(--foot-bottom)}
.bottom-row{left:125px;top:1100px;height:24px;display:flex;align-items:center;white-space:nowrap}
.bottom-brand{font-family:Ubuntu,sans-serif;font-weight:500;font-size:11px;color:#777;margin-right:14px}
.bottom-links{font-size:9.5px;color:#ddd;word-spacing:1px}
.copyright{font-size:9.5px;color:#aaa;margin-left:16px}
</style>
</head>
<body>
<div class="page">
  <div class="abs topline"></div>
  <header class="abs header"></header>
  <div class="abs brand"><span class="brand-dot"></span>RIGSUM SOFTWARE</div>
  <nav class="abs nav">
    <a class="active" href="#">Home</a><a href="#">Product</a><a href="#">Services</a><a href="#">News</a><a href="#">About Us</a><a href="#">Contact Us</a>
  </nav>

  <div class="abs hero" role="img" aria-label="Photo of a young businessman in glasses writing the word Idea with a glowing light bulb on a chalkboard">
    <div class="abs hero-person"></div>
    <div class="abs hero-copy">
      <div class="s">USING NEWEST</div>
      <div class="b">TECHNOLOGY...</div>
      <div class="s">TO</div>
      <div class="b">COMMUNICATE BETTER</div>
    </div>
  </div>
  <div class="abs arrow" style="left:116px;top:257px"><svg width="10" height="14"><path d="M8 1 2 7l6 6" fill="none" stroke="#555" stroke-width="2"/></svg></div>
  <div class="abs arrow" style="left:851px;top:257px"><svg width="10" height="14"><path d="M2 1l6 6-6 6" fill="none" stroke="#555" stroke-width="2"/></svg></div>

  <div class="abs band"></div>
  <div class="abs card" style="left:123px">
    <div class="card-icon"><svg width="24" height="22" fill="#fff"><rect x="2" y="14" width="3" height="7"/><rect x="7" y="11" width="3" height="10"/><rect x="12" y="8" width="3" height="13"/><rect x="17" y="5" width="3" height="16"/><path d="M1 11 9 4l4 3 8-6" stroke="#fff" stroke-width="1.5" fill="none"/></svg></div>
    <div class="ribbon">PLAN</div>
    <p>QTV delivers a standardized, systematic approach to understanding, quantifying and communicating the impact of project risk to all stakeholders.</p>
    <div class="btn">readmore...</div>
  </div>
  <div class="abs card" style="left:316px">
    <div class="card-icon"><svg width="24" height="24" fill="#fff"><rect x="4" y="2" width="2.5" height="20"/><path d="M6.5 3h14l-4 5 4 5h-14z"/></svg></div>
    <div class="ribbon">EXECUTE</div>
    <p>Since 1992 BLZ has been helping companies optimize their materials and logistics processes and accurately track costs on a daily basis.</p>
    <div class="btn">readmore...</div>
  </div>
  <div class="abs card" style="left:508px">
    <div class="card-icon"><svg width="20" height="24" fill="none" stroke="#fff" stroke-width="1.6"><path d="M10 2a6.5 6.5 0 0 0-4 11.6V17h8v-3.4A6.5 6.5 0 0 0 10 2z"/><path d="M7 20h6"/></svg></div>
    <div class="ribbon">LEARN</div>
    <p>BoreMemory is an advanced lessons learned and knowledge management system for use in the Oil &amp; Gas industry. It's fully searchable and easy to use.</p>
    <div class="btn">readmore...</div>
  </div>
  <div class="abs card" style="left:699px">
    <div class="card-icon"><svg width="24" height="16" fill="none" stroke="#fff" stroke-width="2.4"><path d="M8 2 2 8l6 6M16 2l6 6-6 6"/></svg></div>
    <div class="ribbon">EMBED</div>
    <p>Software solutions rely on people and processes to deliver results. From analysis through execution we support our clients to improve performance.</p>
    <div class="btn">readmore...</div>
  </div>

  <h2 class="abs section-title"><span class="ring"><svg width="12" height="12" fill="none" stroke="#fff" stroke-width="1.6"><rect x="1" y="5" width="6" height="3.5" rx="1.7" transform="rotate(-45 4 7)"/><rect x="5" y="3" width="6" height="3.5" rx="1.7" transform="rotate(-45 8 5)"/></svg></span>Who are our customers?</h2>
  <div class="abs clients"></div>
  <div class="abs client" style="left:166px">Prue</div>
  <div class="abs client" style="left:279px">Solvane</div>
  <div class="abs client" style="left:393px">VONI</div>
  <div class="abs client" style="left:506px">SALVEM</div>
  <div class="abs client" style="left:620px">Darrowfield</div>
  <div class="abs client" style="left:734px">Kestmoor</div>
  <div class="abs arrow" style="left:116px;top:805px"><svg width="10" height="14"><path d="M8 1 2 7l6 6" fill="none" stroke="#555" stroke-width="2"/></svg></div>
  <div class="abs arrow" style="left:848px;top:805px"><svg width="10" height="14"><path d="M2 1l6 6-6 6" fill="none" stroke="#555" stroke-width="2"/></svg></div>

  <footer class="abs footer"></footer>
  <div class="abs col-head" style="left:124px"><svg width="14" height="16" fill="#fff"><path d="M7 1a5 5 0 0 0-3 9v2h6v-2a5 5 0 0 0-3-9z"/><rect x="4.5" y="13" width="5" height="2"/></svg>About Rigsum</div>
  <div class="abs foot-text about" style="left:124px;top:946px;width:224px">
    <p>Duis autem vel eum iriure dolor in hendrerit in vulputate velit esse molestie consequat, vel illum dolore eu feugiat nulla facilisis at vero eros et accumsan et iusto odio.</p>
    <p style="margin-top:14px">Et iusto odio dignissim qui blandit praesent luptatum zzril delenit augue duis dolore te feugait nulla facilisi...</p>
  </div>
  <div class="abs divider" style="left:363px"></div>
  <div class="abs col-head" style="left:383px"><svg width="14" height="14" fill="#fff"><rect x="1" y="1" width="12" height="12" rx="1"/><path d="M3.5 4.5h7M3.5 7h7M3.5 9.5h7" stroke="#2a2a2a" stroke-width="1.2"/></svg>Recent News</div>
  <ul class="abs foot-text news" style="left:383px;top:946px;width:180px">
    <li>Duis autem vel eum iriure dolor in hendr eesse molestie...</li>
    <li>Vel eum iriure dolor in hendreesse mol estie consequat praesent ...</li>
    <li>Iriure dolor in hendreesse molestie con sequat praesent...</li>
  </ul>
  <div class="abs divider" style="left:570px"></div>
  <div class="abs col-head" style="left:590px"><svg width="14" height="16" fill="#fff"><circle cx="7" cy="4.5" r="3.5"/><path d="M0 16c0-5 3-7 7-7s7 2 7 7z"/></svg>Contact Us</div>
  <div class="abs contact" style="left:586px;top:948px">
    <div class="office"><svg width="13" height="12" fill="none" stroke="#ccc" stroke-width="1.3"><path d="M1 6 6.5 1 12 6M3 5v6h7V5"/></svg>Europe</div>
    <div class="foot-text" style="margin:4px 0 0 21px">18 Harlow Row<br>Northcairn, NC4 2QP</div>
    <div class="foot-text row" style="margin-top:12px"><svg width="11" height="14" fill="none" stroke="#ccc" stroke-width="1.3"><rect x="1.5" y="1" width="8" height="12" rx="1.5"/></svg>+44(0)1000 555012</div>
    <div class="foot-text row" style="margin-top:10px"><svg width="12" height="10" fill="none" stroke="#ccc" stroke-width="1.3"><rect x="1" y="1" width="10" height="8"/><path d="M1 1l5 4 5-4"/></svg>eu@rigsumsoft.example</div>
  </div>
  <div class="abs divider" style="left:724px"></div>
  <div class="abs contact" style="left:734px;top:948px">
    <div class="office"><svg width="13" height="12" fill="none" stroke="#ccc" stroke-width="1.3"><path d="M1 6 6.5 1 12 6M3 5v6h7V5"/></svg>North America</div>
    <div class="foot-text" style="margin:4px 0 0 21px">1400 Meadowline Dr<br>Suite 200, Fairport, TX 70000</div>
    <div class="foot-text row" style="margin-top:12px"><svg width="11" height="14" fill="none" stroke="#ccc" stroke-width="1.3"><rect x="1.5" y="1" width="8" height="12" rx="1.5"/></svg>(555) 010 4471</div>
    <div class="foot-text row" style="margin-top:10px"><svg width="12" height="10" fill="none" stroke="#ccc" stroke-width="1.3"><rect x="1" y="1" width="10" height="8"/><path d="M1 1l5 4 5-4"/></svg>us@rigsumsoft.example</div>
  </div>

  <div class="abs bottom"></div>
  <div class="abs bottom-row">
    <span class="bottom-brand">RIGSUM SOFTWARE</span>
    <span class="bottom-links">Home &nbsp;|&nbsp; Product &nbsp;|&nbsp; Services &nbsp;|&nbsp; News &nbsp;|&nbsp; About Us &nbsp;|&nbsp; Contact Us &nbsp;|</span>
    <span class="copyright">Copyright © 2013 Tillow Media, Inc. All Rights Reserved.</span>
  </div>
</div>
</body>
</html>
```